Business Card for Multi-Brand Sportswear Company

We are looking for a business card which represents our company and the multiple brands within it.

The company: Kelt Athletic (LTD)
The brands: Kelt, PawaLuni, VerdantFlex, Grit and Gale

Employees using these cards would be representing Kelt Athletic, rather than any of the individual brands. You will see a current design within the uploaded files, to give some inspiration. The actual text of the brands is not necessary, but the logos should be on there is some format.

Our creative minds on this are stretched, so we are looking for someone to make this their own, and show us what a good business card should look like.

We may like to get these printed with spot gloss, so keep that in mind with your designs.

www.keltathletic.co.uk

Industry/Entity Type

Business

Contact Information for Business Card

Tom Hollingsworth-Pryce
Operations Manager
(+44) 1632 960 418
Tom@keltathletic.co.uk
www.keltathletic.co.uk

Font styles to use
Sans Serif
Other font styles liked:
• Eurostile

Colors
ffffff

Requirements
Nice to have
• Dark (black) background

```html
<!DOCTYPE html>
<html lang="en">
<head>
<meta charset="utf-8">
<title>Kelt Athletic – Business Card</title>
<link rel="stylesheet" href="https://fonts.googleapis.com/css2?family=Michroma&display=swap">
<style>
  :root {
    --canvas: #e9e6e1;
    --black: #0d0d0d;
    --black-soft: #1e1e1e;
    --white: #ffffff;
    --paper: #f4f4f4;
    --red: #e3262b;
    --red-light: #f0585a;
    --ink: #141414;
    --grey: #8d8d8d;
    --silver: #c9c9c9;
  }
  * { margin: 0; padding: 0; box-sizing: border-box; }
  html, body { width: 771px; height: 1200px; overflow: hidden; }
  body {
    background: var(--canvas);
    font-family: "Michroma", "Eurostile", sans-serif;
    display: flex;
    align-items: center;
    justify-content: center;
    gap: 40px;
  }
  .card {
    position: relative;
    width: 320px;
    height: 528px;
    overflow: hidden;
    box-shadow: 0 10px 30px rgba(0,0,0,.18);
  }

  /* Front */
  .card-front { background: var(--paper); }
  .front-art { position: absolute; inset: 0; width: 100%; height: 100%; }
  .front-brand {
    position: absolute;
    top: 48px;
    right: 24px;
    text-align: right;
    color: var(--white);
  }
  .front-brand .brand-name { font-size: 19px; letter-spacing: 1px; }
  .front-brand .brand-tag { font-size: 6.5px; letter-spacing: 1.6px; color: var(--silver); margin-top: 4px; }

  .contact-block { position: absolute; top: 218px; left: 24px; right: 20px; }
  .person-name { font-size: 15px; color: var(--ink); letter-spacing: .2px; line-height: 1.25; }
  .person-name .surname-tail { color: var(--red); }
  .person-role { font-size: 9px; color: var(--red); margin-top: 4px; }
  .role-rule { height: 1px; background: var(--red); width: 210px; margin-top: 7px; }
  .contact-list { list-style: none; margin-top: 18px; }
  .contact-list li {
    display: flex; align-items: center; gap: 10px;
    font-size: 9.5px; color: var(--ink); margin-bottom: 10px;
  }
  .contact-list svg { width: 11px; height: 11px; flex: none; }

  .brand-row {
    position: absolute;
    left: 18px; right: 18px; bottom: 34px;
    display: flex; justify-content: space-between; align-items: center;
  }
  .sub-brand {
    display: flex; align-items: center; gap: 4px;
    font-size: 6.5px; color: var(--grey); letter-spacing: .3px;
  }
  .sub-brand .dot { width: 6px; height: 6px; border-radius: 50%; background: var(--grey); }

  /* Back */
  .card-back {
    background: linear-gradient(125deg, var(--black) 0%, var(--black-soft) 55%, var(--black) 100%);
    display: flex; flex-direction: column; align-items: center; justify-content: center;
    color: var(--white);
  }
  .back-brand .brand-name { font-size: 36px; letter-spacing: 2px; text-align: center; color: var(--silver); }
  .back-brand .brand-sub { font-size: 14px; letter-spacing: 5px; text-align: center; color: var(--white); margin-top: 6px; }
  .back-brand .brand-tag { font-size: 7px; letter-spacing: 2.4px; text-align: center; color: var(--grey); margin-top: 10px; }
</style>
</head>
<body>

  <section class="card card-front" aria-label="Business card front">
    <svg class="front-art" viewBox="0 0 320 528" preserveAspectRatio="none" aria-hidden="true">
      <defs>
        <linearGradient id="top-dark" x1="0" y1="0" x2="1" y2="1">
          <stop offset="0" stop-color="#0d0d0d"/>
          <stop offset="1" stop-color="#262626"/>
        </linearGradient>
        <linearGradient id="swoosh" x1="0" y1="0" x2="1" y2="0">
          <stop offset="0" stop-color="#f0585a"/>
          <stop offset="1" stop-color="#e3262b"/>
        </linearGradient>
      </defs>
      <path d="M0 0 H320 V200 C250 200 200 110 120 95 C70 86 30 92 0 100 Z" fill="url(#top-dark)"/>
      <path d="M0 100 C30 92 70 86 120 95 C200 110 250 200 320 200 V222 C240 220 200 140 120 122 C70 112 30 118 0 128 Z" fill="url(#swoosh)"/>
    </svg>

    <div class="front-brand">
      <div class="brand-name">KELT ATHLETIC</div>
      <div class="brand-tag">PERFORMANCE WEAR</div>
    </div>

    <div class="contact-block">
      <h1 class="person-name">Tom Hollingsworth<span class="surname-tail">-Pryce</span></h1>
      <p class="person-role">Operations Manager</p>
      <div class="role-rule"></div>
      <ul class="contact-list">
        <li>
          <svg viewBox="0 0 12 12" aria-hidden="true"><path d="M1 4 C1 2 3 1 6 1 C9 1 11 2 11 4 L9 5 L8 3.5 H4 L3 5 Z M3 6 H9 L10 11 H2 Z" fill="var(--red)"/></svg>
          <span>(+44) 1632 960 418</span>
        </li>
        <li>
          <svg viewBox="0 0 12 12" aria-hidden="true"><rect x="1" y="2.5" width="10" height="7" fill="var(--red)"/><path d="M1 2.5 L6 6.5 L11 2.5" fill="none" stroke="var(--paper)" stroke-width="1"/></svg>
          <span>Tom@keltathletic.co.uk</span>
        </li>
        <li>
          <svg viewBox="0 0 12 12" aria-hidden="true"><circle cx="6" cy="6" r="5" fill="none" stroke="var(--red)" stroke-width="1.2"/><ellipse cx="6" cy="6" rx="2" ry="5" fill="none" stroke="var(--red)" stroke-width="1"/><line x1="1" y1="6" x2="11" y2="6" stroke="var(--red)" stroke-width="1"/></svg>
          <span>www.keltathletic.co.uk</span>
        </li>
      </ul>
    </div>

    <div class="brand-row" aria-label="Group brands">
      <span class="sub-brand"><span class="dot"></span>PawaLuni</span>
      <span class="sub-brand">Grit and Gale</span>
      <span class="sub-brand">Kelt</span>
      <span class="sub-brand">VerdantFlex</span>
    </div>
  </section>

  <section class="card card-back" aria-label="Business card back">
    <div class="back-brand">
      <div class="brand-name">KELT</div>
      <div class="brand-sub">ATHLETIC</div>
      <div class="brand-tag">PERFORMANCE WEAR</div>
    </div>
  </section>

</body>
</html>
```